*** Business Card Design Project

I need a logo and business card for my new catering business: "Pomelia". The design should be modern, clean, elegant and refined. One or Two colours only. The design SHOULD NOT include graphics or images. There should be space for my name, phone number and email address (I will provide these to you later).

Industry/Entity Type

Catering

Requirements
Must have
• Must have one or two colours only.
Must include the text "pomelia"
Should not have
• Must not have graphics or images.

```html
<!DOCTYPE html>
<html lang="en">
<head>
<meta charset="utf-8">
<title>Pomelia – Business Card</title>
<link rel="stylesheet" href="https://fonts.googleapis.com/css2?family=Questrial&family=Open+Sans:wght@600&display=swap">
<style>
  :root {
    --leaf-green: #a2cb39;
    --paper: #ffffff;
    --ink-light: #ffffff;
  }
  html, body {
    margin: 0;
    padding: 0;
    width: 1200px;
    height: 741px;
    overflow: hidden;
    background: var(--paper);
  }
  .card {
    position: relative;
    width: 1200px;
    height: 741px;
    background: var(--paper);
  }
  .brand {
    position: absolute;
    display: flex;
    align-items: center;
    font-family: "Questrial", sans-serif;
    font-weight: 400;
    line-height: 1;
  }
  .brand-dot {
    border-radius: 50%;
    flex: none;
  }
  .brand--header {
    left: 0;
    width: 1200px;
    top: 95px;
    justify-content: center;
    gap: 26px;
    color: var(--leaf-green);
    font-size: 112px;
  }
  .brand--header .brand-dot {
    width: 92px;
    height: 92px;
    background: var(--leaf-green);
  }
  .band {
    position: absolute;
    left: 0;
    top: 269px;
    width: 1200px;
    height: 448px;
    background: var(--leaf-green);
    color: var(--ink-light);
  }
  .person-name {
    position: absolute;
    left: 0;
    width: 1200px;
    top: 58px;
    margin: 0;
    text-align: center;
    font-family: "Questrial", sans-serif;
    font-weight: 400;
    font-size: 68px;
    letter-spacing: 1px;
  }
  .person-role {
    position: absolute;
    left: 620px;
    top: 141px;
    margin: 0;
    font-family: "Questrial", sans-serif;
    font-size: 36px;
  }
  .contact {
    position: absolute;
    left: 64px;
    top: 280px;
    margin: 0;
    padding: 0;
    list-style: none;
    font-family: "Open Sans", sans-serif;
    font-weight: 600;
    font-size: 24px;
    line-height: 40px;
  }
  .contact .address {
    line-height: 33px;
    margin-top: 2px;
  }
  .brand--footer {
    left: 820px;
    top: 355px;
    gap: 12px;
    color: var(--ink-light);
    font-size: 58px;
  }
  .brand--footer .brand-dot {
    width: 48px;
    height: 48px;
    background: var(--ink-light);
  }
</style>
</head>
<body>
  <div class="card">
    <div class="brand brand--header">
      <span class="brand-dot" aria-hidden="true"></span>
      <span class="brand-name">Pomelia</span>
    </div>

    <section class="band">
      <h1 class="person-name">Liam Harrow</h1>
      <p class="person-role">- Proprieter</p>

      <ul class="contact">
        <li>Phone : 0061 987654321</li>
        <li>E-mail : info@pomeliacatering.com</li>
        <li class="address">Address : Harrow Kitchens Pty Ltd, Level 2,<br>18 Vine Lane, Redfern 2016, NSW Australia</li>
      </ul>

      <div class="brand brand--footer">
        <span class="brand-dot" aria-hidden="true"></span>
        <span class="brand-name">Pomelia</span>
      </div>
    </section>
  </div>
</body>
</html>
```